Website Templates Design Project

BrawnLoop Template Websites
Creative Brief

BrawnLoop Gyms
The growth of BrawnLoop Gyms (or boxes, as they are called by members) is an amazing world-wide phenomenon. More than 3,400 gyms ranging from “garage gyms” to massive retail locations have opened in recent years. The philosophy for workouts at the gym is built around is “constantly varied (if not random), high intensity, functional movement". Each gym does what is called a WOD, or Workout of the Day. Workouts are typically short—20 minutes or less—and intense, demanding all-out physical exertion.
The growth of the gyms, mainly in the United States, has generally come from military veterans, police officers and fireman. However, BrawnLoop box owners are mostly trainers and not necessarily skilled in operating or marketing a business. Our company is launching a new platform for boxes to purchase inexpensive template websites and other marketing materials.
The Need
Most BrawnLoop box owners have launched with basic WordPress websites. We see an opportunity to provide more dynamic and professional websites, using a template and content management system. We aim to offer multiple template designs (not WordPress) for box owners. The platform that we are using can be found at www.sitekitpreview7.com. We are looking for graphic designs that will fit this platform.
A big part of the BrawnLoop philosophy is built around an Internet-based community. Therefore, our website templates should allow for a robust blog that allows for posting of pictures and video by members and the box owner.
The Designs
We strongly encourage designers to review other BrawnLoop websites for design ideas and functionality (good and bad).
We are looking for cutting-edge designs. One person on our team said, “these sites need to be so good that they sweat!” Obviously, imagery that portrays working out and muscles will be attractive to box owners. Many of the graphics for BrawnLoop sites use particularly masculine images like diamond plate and steel. The designs should be contemporary and at first glance you show know that this is a BrawnLoop website.
Rotating images and video windows are good, just nothing that will require long load times.

Images and Logos
Please don’t pirate logos ad images from BrawnLoop sites without permission. For your design submissions, feel free to develop generic logos and names for BrawnLoop Gyms. If you use and stock photography, please indicate whether you have permission to use or where permission can be obtained.

The navigation for a basic website design (and your designs) should include:
Home (with WOD blog dominating body of page)
About Us
Store
Membership Info (with link to store)
Directions
Contact Us

Target Market(s)

18-35, athletic types, male and female

Industry/Entity Type

Marketing

Requirements
Must have
• Navigation "buttons":

About Us
Store
Directions
Contact Us

```html
<!DOCTYPE html>
<html lang="en">
<head>
<meta charset="utf-8">
<title>BrawnLoop Gyms</title>
<link href="https://fonts.googleapis.com/css2?family=Open+Sans:ital,wght@0,400;0,600;0,700;0,800;1,400&family=Bree+Serif&family=Oswald:wght@500;700&display=swap" rel="stylesheet">
<style>
:root{
  --dark:#1c1c1c;
  --nav:#2f2f2f;
  --blue:#0b8fd6;
  --green:#6ab43a;
  --orange:#ef7a12;
  --tan:#d79a45;
  --red:#cf4b55;
  --purple:#8b66c9;
  --page:#ececec;
  --white:#ffffff;
  --text:#444;
  --muted:#888;
  --line:#dcdcdc;
  --grey:#8a8a8a;
}
*{box-sizing:border-box;margin:0;padding:0}
html,body{width:1200px;height:3338px;overflow:hidden}
body{position:relative;background:var(--page);font-family:"Open Sans",Arial,sans-serif;color:var(--text);font-size:12px}
.abs{position:absolute}
/* header */
.site-header{left:0;top:0;width:1200px;height:123px;background:linear-gradient(#262626,#151515)}
.brand{left:140px;top:42px;display:flex;align-items:center;gap:10px;color:#fff;font-weight:800;font-size:32px;letter-spacing:-.5px}
.brand-dot{width:20px;height:20px;border-radius:50%;background:var(--blue)}
.top-links{left:668px;top:14px;font-size:10px;color:#aaa;white-space:nowrap}
.top-links b{color:var(--orange)}
.join{left:990px;top:-20px;width:66px;height:66px;border-radius:50%;background:var(--green);color:#fff;font-size:13px;font-weight:700;text-align:center;padding-top:32px}
.social{left:808px;top:76px;display:flex;gap:22px;color:#bbb;font-size:14px;font-weight:700}
.social span{display:flex;align-items:center;gap:7px}
.social i{width:18px;height:18px;border-radius:50%;background:#555;display:inline-block}
.main-nav{left:0;top:123px;width:1200px;height:50px;background:var(--nav);border-top:1px solid #444}
.main-nav ul{list-style:none;position:absolute;left:140px;top:0;display:flex;height:50px}
.main-nav li{color:#ddd;font-size:16px;line-height:50px;padding:0 26px}
.main-nav li.active{background:var(--blue);color:#fff;padding:0 22px}
/* container */
.container{left:140px;top:173px;width:920px;height:2810px;background:var(--white)}
.slider{left:145px;top:190px;width:910px;height:413px;background:#101010;border:4px solid #222}
.slider-photo{position:absolute;inset:0;background:linear-gradient(90deg,#e9e9e9 0%,#c8c8c8 35%,#7a7a7a 60%,#b8b8b8 100%)}
.slides{position:absolute;left:16px;top:16px;width:298px}
.slide-tab{height:57px;margin-bottom:5px;color:#fff;font-weight:700;font-size:17px;line-height:21px;padding:7px 12px}
.t1{background:var(--green)}.t2{background:#2da5e0}.t3{background:var(--tan)}.t4{background:var(--red)}.t5{background:var(--purple)}
/* posts */
.post{left:140px;width:605px;height:572px}
.date-badge{position:absolute;left:0;top:0;width:47px;height:50px;background:var(--blue);color:#fff;font-size:9px;font-weight:700;text-align:center;padding-top:12px;line-height:13px}
.post-title{position:absolute;left:61px;top:0;font-family:"Bree Serif",Georgia,serif;font-size:21px;color:#222;line-height:27px;width:400px;font-weight:400}
.post-photo{position:absolute;left:19px;top:72px;width:584px;height:268px;border:6px solid #e4e4e4;background:linear-gradient(90deg,#dfe6ea,#b9c3c9 40%,#e7d3c6 70%,#c7cfd6)}
.post-meta{position:absolute;left:19px;top:355px;font-size:10px;color:var(--muted);display:flex;gap:60px}
.post-meta span::before{content:"";display:inline-block;width:9px;height:9px;border:1px solid #aaa;border-radius:50%;margin-right:6px;vertical-align:-1px}
.post-text{position:absolute;left:19px;top:378px;width:580px;font-size:12px;line-height:18px;color:#555}
.share{position:absolute;left:19px;top:472px;font-size:12px;color:#333;display:flex;align-items:center;gap:6px}
.share-btn{border:1px solid #bbb;border-radius:3px;padding:0 6px;font-size:10px;color:#2a6fb0;background:#f7f7f7}
.like{position:absolute;left:19px;top:500px;display:flex;gap:6px;font-size:10px}
.like span{border:1px solid #aac;border-radius:2px;padding:0 5px;background:#eef}
.post-rule{position:absolute;left:19px;top:545px;width:584px;border-top:1px solid var(--line)}
.pager{left:350px;top:2926px;display:flex;gap:5px;font-size:11px;color:#555;align-items:center}
.pager b{width:18px;height:18px;border:1px solid #ccc;text-align:center;line-height:16px;font-weight:400}
.pager b.on{background:var(--orange);color:#fff;border-color:var(--orange)}
/* sidebar */
.widget-head{left:773px;width:265px;height:32px;color:#fff;font-weight:700;font-size:15px;padding:5px 10px}
.cats{left:773px;top:688px;width:265px;list-style:none}
.cats li{height:31px;border-bottom:1px solid #e6e6e6;font-size:10px;color:#555;padding-left:24px;line-height:30px;position:relative}
.cats li::before{content:"";position:absolute;left:6px;top:10px;width:10px;height:10px;border-radius:50%;background:#ddd;border:1px solid #bbb}
.video{left:785px;top:1015px;width:245px;height:142px;background:linear-gradient(120deg,#8a4a50,#c9c3c2 60%,#6e6c70)}
.play{position:absolute;left:102px;top:50px;width:42px;height:42px;border-radius:50%;background:#e32}
.play::after{content:"";position:absolute;left:16px;top:12px;border-left:14px solid #fff;border-top:9px solid transparent;border-bottom:9px solid transparent}
.events{left:785px;top:1232px;width:245px;list-style:none}
.events li{font-size:10px;line-height:15px;color:#666;padding:10px 0 11px 12px;border-bottom:1px solid #e6e6e6;position:relative}
.events li::before{content:"•";position:absolute;left:2px}
.read-all{left:805px;top:1455px;background:var(--blue);color:#fff;font-size:10px;padding:3px 10px}
.testimonial{left:789px;top:1548px;width:240px;font-size:10px;line-height:16px;font-style:italic;color:#666}
.testimonial p{margin-bottom:14px}
.newsletter-title{left:797px;top:1742px;font-family:"Oswald",Impact,sans-serif;font-weight:700;font-size:26px;color:#333}
.nl-ico{left:990px;top:1750px;width:28px;height:22px;border:2px solid #c44;background:#fff}
.field{left:800px;width:225px;height:28px;border-radius:14px;background:#e9e9e9;border:1px solid #ccc;font-size:11px;color:#777;padding:5px 14px}
.submit{left:797px;top:1888px;font-family:"Oswald",Impact,sans-serif;font-weight:700;font-size:26px;color:#bbb}
.ad{left:800px;top:1945px;width:225px;height:190px;background:linear-gradient(#d8dde2,#9aa4ad 60%,#5a2a2a)}
.ad-copy{position:absolute;left:10px;top:20px;font-family:"Oswald",Impact,sans-serif;color:#111;font-size:22px;line-height:24px;font-weight:700}
.ad-tag{position:absolute;right:10px;bottom:12px;background:#c02;color:#fff;font-size:13px;font-weight:700;padding:3px 8px}
.fb-box{left:800px;top:2185px;width:222px;height:275px;border:1px solid #bbb;background:#fff;font-size:10px;padding:8px}
.fb-top{display:flex;gap:8px}
.fb-top i{width:42px;height:42px;background:#3a5a9a;display:block;flex:none}
.fans{display:grid;grid-template-columns:repeat(5,1fr);gap:3px 5px;margin-top:12px}
.fans div{height:40px;background:#b8bcc4}
.fans span{font-size:8px;color:#3b5998;height:12px;line-height:12px}
/* footer */
.site-footer{left:0;top:3008px;width:1200px;height:330px;background:linear-gradient(#2b2b2b,#1a1a1a)}
.foot-nav{position:absolute;left:0;width:1200px;top:20px;text-align:center;font-size:11px;color:#ccc;word-spacing:4px}
.foot-nav::after{content:"";position:absolute;left:140px;right:140px;top:28px;border-top:1px solid #3d3d3d}
.fcol{position:absolute;top:72px;font-size:10px;line-height:15px;color:#8a8a8a}
.fcol h4{font-size:14px;color:var(--blue);margin-bottom:10px;font-weight:700}
.fcol .d{color:#bbb;font-style:italic}
.fcol p{margin-bottom:12px}
.soc-row{display:flex;align-items:center;gap:10px;margin-bottom:12px;color:#bbb}
.soc-row i{width:22px;height:22px;border-radius:3px;display:block}
.copy{position:absolute;right:140px;top:302px;font-size:10px;color:#777}
</style>
</head>
<body>

<header class="abs site-header">
  <div class="abs brand">BrawnLoop <span class="brand-dot"></span> GYMS</div>
  <div class="abs top-links">Existing client? <b>Login here.</b> &nbsp; Want to work with us? <b>Click here</b></div>
  <div class="abs join">JOIN US</div>
  <div class="abs social"><span><i></i>CHIRPLINE</span><span><i></i>FRIENDWALL</span><span><i></i>RSS</span></div>
</header>
<nav class="abs main-nav">
  <ul><li class="active">HOME</li><li>ABOUT US</li><li>STORE</li><li>MEMBERSHIP INFO</li><li>DIRECTIONS</li><li>CONTACT US</li></ul>
</nav>

<div class="abs container"></div>

<section class="abs slider">
  <div class="slider-photo" role="img" aria-label="Athlete seated on a bench with dumbbells in a gym"></div>
  <div class="slides">
    <div class="slide-tab t1">Neque porro quisquam est qui dolorem ipsum...</div>
    <div class="slide-tab t2">Dolor sit amet, consectetur, adipisci veli..</div>
    <div class="slide-tab t3">Det er en kendsgerning, at man bliver distraheret...</div>
    <div class="slide-tab t4">Rolf Brandvik, profso i latin fra Hampden...</div>
    <div class="slide-tab t5">Alle Lorem Ipsum-generat pnettet har en tendens til...</div>
  </div>
</section>

<article class="abs post" style="top:628px">
  <div class="date-badge">JUN 30<br>2011</div>
  <h2 class="post-title">Donec vulputate nulla in nibh pellentesque consequat.</h2>
  <div class="post-photo" role="img" aria-label="Man curling a dumbbell with a class training behind him"></div>
  <div class="post-meta"><span>June 30, 2011</span><span>No Comments</span></div>
  <p class="post-text">Lorem ipsum dolor sit amet, consectetuer adipiscing elit. Donec semper risus id neque vulp elementum. Ut diam neque, vestibulum non, sagittis quis, commodo id, purus. Vivamus sagittis, odio non rhoncus adipiscing, elit ipsum pulvinar est, vitae malesuada velit orci sed arcu. Nulla facilisi. Integer vulputate pretium neque. Nulla aliquam orci non neque. Fusce tempor placerat [...]</p>
  <div class="share">Share: <span class="share-btn">Share</span></div>
  <div class="like"><span>Like</span><span>2</span></div>
  <div class="post-rule"></div>
</article>

<article class="abs post" style="top:1200px">
  <div class="date-badge">JUN 30<br>2011</div>
  <h2 class="post-title">Donec vulputate nulla in nibh pellentesque consequat.</h2>
  <div class="post-photo" role="img" aria-label="Group class lifting barbells overhead" style="background:linear-gradient(90deg,#c9a79a,#e5e0dc 30%,#b7c0cc 60%,#d9c2b5)"></div>
  <div class="post-meta"><span>June 30, 2011</span><span>No Comments</span></div>
  <p class="post-text">Lorem ipsum dolor sit amet, consectetuer adipiscing elit. Donec semper risus id neque vulp elementum. Ut diam neque, vestibulum non, sagittis quis, commodo id, purus. Vivamus sagittis, odio non rhoncus adipiscing, elit ipsum pulvinar est, vitae malesuada velit orci sed arcu. Nulla facilisi. Integer vulputate pretium neque. Nulla aliquam orci non neque. Fusce tempor placerat [...]</p>
  <div class="share">Share: <span class="share-btn">Share</span></div>
  <div class="like"><span>Like</span><span>2</span></div>
  <div class="post-rule"></div>
</article>

<article class="abs post" style="top:1772px">
  <div class="date-badge">JUN 30<br>2011</div>
  <h2 class="post-title">Donec vulputate nulla in nibh pellentesque consequat.</h2>
  <div class="post-photo" role="img" aria-label="Man curling a dumbbell with a class training behind him"></div>
  <div class="post-meta"><span>June 30, 2011</span><span>No Comments</span></div>
  <p class="post-text">Lorem ipsum dolor sit amet, consectetuer adipiscing elit. Donec semper risus id neque vulp elementum. Ut diam neque, vestibulum non, sagittis quis, commodo id, purus. Vivamus sagittis, odio non rhoncus adipiscing, elit ipsum pulvinar est, vitae malesuada velit orci sed arcu. Nulla facilisi. Integer vulputate pretium neque. Nulla aliquam orci non neque. Fusce tempor placerat [...]</p>
  <div class="share">Share: <span class="share-btn">Share</span></div>
  <div class="like"><span>Like</span><span>2</span></div>
  <div class="post-rule"></div>
</article>

<article class="abs post" style="top:2344px">
  <div class="date-badge">JUN 30<br>2011</div>
  <h2 class="post-title">Donec vulputate nulla in nibh pellentesque consequat.</h2>
  <div class="post-photo" role="img" aria-label="Group class lifting barbells overhead" style="background:linear-gradient(90deg,#c9a79a,#e5e0dc 30%,#b7c0cc 60%,#d9c2b5)"></div>
  <div class="post-meta"><span>June 30, 2011</span><span>No Comments</span></div>
  <p class="post-text">Lorem ipsum dolor sit amet, consectetuer adipiscing elit. Donec semper risus id neque vulp elementum. Ut diam neque, vestibulum non, sagittis quis, commodo id, purus. Vivamus sagittis, odio non rhoncus adipiscing, elit ipsum pulvinar est, vitae malesuada velit orci sed arcu. Nulla facilisi. Integer vulputate pretium neque. Nulla aliquam orci non neque. Fusce tempor placerat [...]</p>
  <div class="share">Share: <span class="share-btn">Share</span></div>
  <div class="like"><span>Like</span><span>2</span></div>
</article>

<div class="abs pager">« Prev <b class="on">1</b><b>2</b><b>3</b><b>4</b><b>5</b> Next »</div>

<h3 class="abs widget-head" style="top:650px;background:var(--orange)">Categories</h3>
<ul class="abs cats">
  <li>DIETS</li><li>FITNESS</li><li>GUIDES</li><li>MUSCLE</li><li>NUTRITION</li><li>RECIPES</li><li>TRAINING</li><li>WEIGHTS</li><li>WORKOUTS</li>
</ul>

<h3 class="abs widget-head" style="top:970px;background:var(--green)">Recent Video</h3>
<div class="abs video" role="img" aria-label="Workout video still"><span class="play"></span></div>

<h3 class="abs widget-head" style="top:1186px;background:#1b9be0">Upcoming Events</h3>
<ul class="abs events">
  <li>Lorem ipsum dolor sit amet, conse er adipiscing elit. Donec semid...</li>
  <li>Lorem ipsum dolor sit amet, conse er adipiscing elit. Donec semid...</li>
  <li>Lorem ipsum dolor sit amet, conse er adipiscing elit. Donec semid...</li>
  <li>Lorem ipsum dolor sit amet, conse er adipiscing elit. Donec semid...</li>
</ul>
<div class="abs read-all">Read all Events »</div>

<h3 class="abs widget-head" style="top:1500px;background:var(--grey)">Client Testimonials</h3>
<div class="abs testimonial">
  <p>"Lorem Ipsum er ganske enkelt fyldtekst fra print- og typografiindustrien. Lorem Ipsum har været standard fyldtekst siden 1500.</p>
  <p>Teltet, hver en ukendt trykker sammensatte en tilfældig spalte for at trykke en bog til sammenligning af forskellige skrifttyper."</p>
  <p>- Client Name Goes Here</p>
</div>

<div class="abs newsletter-title">FREE NEWSLETTER</div>
<div class="abs nl-ico"></div>
<div class="abs field" style="top:1800px">Name:</div>
<div class="abs field" style="top:1840px">Email address:</div>
<div class="abs submit">SUBMIT »</div>

<div class="abs ad" role="img" aria-label="Apparel promotion with athletes in hooded tops">
  <div class="ad-copy">IT'S COOL. STAY WARM.<br>SHOP NOW.</div>
  <div class="ad-tag">Stridewell</div>
</div>

<div class="abs fb-box">
  <div class="fb-top"><i></i><div><b style="color:#3b5998">BrawnLoop Gyms</b> on Friendwall<br><span style="border:1px solid #ccc;padding:0 4px">Like</span></div></div>
  <div style="margin-top:8px">171 people like BrawnLoop Gyms - BrawnLoop Websites.</div>
  <div class="fans">
    <div></div><div></div><div></div><div></div><div></div>
    <span>Ana</span><span>Tom</span><span>Lee</span><span>Sam</span><span>Eve</span>
    <div></div><div></div><div></div><div></div><div></div>
    <span>Ida</span><span>Max</span><span>Kai</span><span>Joe</span><span>Liv</span>
  </div>
  <div style="margin-top:6px;color:#888">Social plugin</div>
</div>

<footer class="abs site-footer">
  <div class="foot-nav">Home &nbsp;| &nbsp;About Us &nbsp;| &nbsp;Store &nbsp;| &nbsp;Membership Info &nbsp;| &nbsp;Directions &nbsp;| &nbsp;Contact Us</div>
  <div class="fcol" style="left:140px;width:220px">
    <h4>Latest News</h4>
    <p><span class="d">2012, June 30</span><br>Lorem ipsum dolor sit amet, conse er adipiscing elit. Donec semid...</p>
    <p><span class="d">2012, June 30</span><br>Lorem ipsum dolor sit amet, conse er adipiscing elit. Donec semid...</p>
    <p><span class="d">2012, June 30</span><br>Lorem ipsum dolor sit amet, conse er adipiscing elit. Donec semid...</p>
  </div>
  <div class="fcol" style="left:524px;width:240px">
    <h4>Quick Contacts</h4>
    <p>BrawnLoop GYMS,<br>Lorem Ipsum is simply dummy text,<br>Lorem Ipsum is simply dummy text.</p>
    <p style="margin-top:46px;color:#bbb">T: 00 555 010 2468<br>M: info@brawnloopgyms.test</p>
  </div>
  <div class="fcol" style="left:868px;width:200px">
    <h4>Stay Connected With Us</h4>
    <div class="soc-row"><i style="background:#3b5998"></i>Friendwall</div>
    <div class="soc-row"><i style="background:#29a9e1"></i>Chirpline</div>
    <div class="soc-row"><i style="background:#f08a24"></i>RSS</div>
  </div>
  <div class="copy">Copyright © 2012 BrawnLoop GYMS</div>
</footer>

</body>
</html>
```